Fall by my site ads for Facebook

I run an events and exhibition company in Singapore and we are trying to build a presence on Facebook. But my colleagues and I are not very good with web banner and Facebook ad designs so most of our postings are boring and doesn't hit the crowd. So I would like to outsource the design of a series of 3 x banner ad or Facebook posting that creates awareness and bring viewers to my website www.plumtavo.com. Our business is of a B2B nature and our clients are typically well-educated young professionals age 25 to 40 and are social media savvy. They are usually from the Marketing, PR, Communications or Media verticals and typically browse Facebook and Instagram at least once a day.

Target Market(s)

well-educated young professionals age 25 to 40 and are social media savvy. They are usually from the Marketing, PR, Communications or Media verticals and typically browse Facebook and Instagram at least once a day.

Industry/Entity Type

Events

Requirements
Must have
• Our website www.plumtavo.com

```html
<!DOCTYPE html>
<html lang="en">
<head>
<meta charset="utf-8">
<title>Think Big Win The World</title>
<link rel="stylesheet" href="https://fonts.googleapis.com/css2?family=Quicksand:wght@300;400&display=swap">
<style>
  :root {
    --night-blue: #1c1bd6;
    --deep-indigo: #120c6e;
    --violet: #7a1fb8;
    --shadow: #0a0b26;
    --teal-glow: #1f6f78;
    --street-red: #d4202a;
    --street-amber: #e0692a;
    --ink-white: #ffffff;
    --globe-blue: #1f6fd1;
  }
  * { margin: 0; padding: 0; box-sizing: border-box; }
  html, body {
    width: 1200px;
    height: 627px;
    overflow: hidden;
    background: var(--shadow);
  }
  .banner {
    position: relative;
    width: 1200px;
    height: 627px;
    overflow: hidden;
    font-family: "Quicksand", sans-serif;
    color: var(--ink-white);
  }
  .city-backdrop {
    position: absolute;
    inset: 0;
    background:
      radial-gradient(ellipse 260px 60px at 30% 88%, rgba(224,105,42,0.55), transparent 70%),
      radial-gradient(ellipse 700px 70px at 20% 90%, rgba(212,32,42,0.75), transparent 70%),
      radial-gradient(ellipse 500px 60px at 85% 84%, rgba(224,105,42,0.45), transparent 70%),
      radial-gradient(ellipse 260px 150px at 45% 62%, rgba(31,111,120,0.75), transparent 70%),
      radial-gradient(ellipse 180px 120px at 15% 55%, rgba(224,105,42,0.35), transparent 70%),
      radial-gradient(ellipse 300px 260px at 100% 30%, rgba(122,31,184,0.9), transparent 70%),
      radial-gradient(ellipse 420px 320px at 70% 40%, rgba(10,11,38,0.85), transparent 70%),
      radial-gradient(ellipse 300px 240px at 50% 45%, rgba(10,11,38,0.6), transparent 70%),
      linear-gradient(180deg, var(--night-blue) 0%, var(--deep-indigo) 40%, var(--shadow) 75%, #1a0a1e 100%);
  }
  .headline {
    position: absolute;
    left: 0;
    width: 1200px;
    text-align: center;
    font-weight: 300;
    font-size: 108px;
    line-height: 1;
    letter-spacing: 14px;
    padding-left: 14px;
    text-transform: uppercase;
    white-space: nowrap;
  }
  .headline-top {
    top: 234px;
    word-spacing: 20px;
  }
  .headline-bottom {
    top: 395px;
    display: flex;
    justify-content: center;
    align-items: center;
  }
  .headline-bottom .word-the {
    margin-right: 111px;
  }
  .globe-letter {
    width: 104px;
    height: 104px;
    margin-left: -9px;
    margin-right: 12px;
    flex: none;
  }
  .site-address {
    position: absolute;
    top: 357px;
    left: 0;
    width: 1200px;
    text-align: center;
    font-weight: 400;
    font-size: 22px;
    letter-spacing: 15px;
    padding-left: 15px;
    text-transform: uppercase;
    white-space: nowrap;
    opacity: 0.9;
  }
</style>
</head>
<body>
  <main class="banner">
    <div class="city-backdrop" role="img" aria-label="Blurred city skyline at night with glowing lights and red light trails along the street"></div>

    <h1 class="headline headline-top">Think Big Win</h1>

    <p class="site-address">www.plumtavo.com</p>

    <p class="headline headline-bottom">
      <span class="word-the">The</span>
      <span>W</span>
      <svg class="globe-letter" viewBox="0 0 106 106" role="img" aria-label="Globe standing in for the letter O">
        <circle cx="53" cy="53" r="50" fill="var(--globe-blue)" stroke="var(--ink-white)" stroke-width="5"/>
      </svg>
      <span>rld</span>
    </p>
  </main>
</body>
</html>
```